Buch-/eBook-Cover zum Thema Geldmanagement
Zielgruppe
ich benötige ein Buch-Cover (Vorder- und Rückseite) für das Buch Der Pfad der klaren Vermögensführung. Untertitel ist Innere Ruhe und Wohlstand vereint. Das genaue Format ist im Briefing hinterlegt
Aufgabenstellung
Schön wäre es, wenn das Cover hell gehalten wäre. Es soll hochwertig aussehen. Ich habe zwar eigenes Bild-Material angegeben, es können jedoch auch andere Vorschläge kommen.

```html
<!DOCTYPE html>
<html lang="de">
<head>
<meta charset="utf-8">
<title>Der Pfad der klaren Vermögensführung – Cover</title>
<link rel="stylesheet" href="https://fonts.googleapis.com/css2?family=Bebas+Neue&family=Open+Sans:wght@400;600;700&display=swap">
<style>
  :root {
    --stage: #e9e9ea;
    --cover-top: #f7f7f8;
    --cover-bottom: #e4e5e8;
    --gold: #c9a331;
    --ink: #1d1d1f;
    --panel: rgba(255,255,255,0.9);
    --stone: #d9dadd;
    --coin: #b7b293;
  }
  * { box-sizing: border-box; margin: 0; padding: 0; }
  html, body { width: 1200px; height: 800px; overflow: hidden; }
  body {
    background: var(--stage);
    display: flex; align-items: center; justify-content: center; gap: 60px;
    font-family: "Open Sans", sans-serif; color: var(--ink);
  }
  .cover {
    position: relative; width: 420px; height: 620px;
    background: radial-gradient(ellipse at 50% 70%, #ffffff 0%, var(--cover-top) 45%, var(--cover-bottom) 100%);
    box-shadow: 0 10px 30px rgba(0,0,0,0.18);
    overflow: hidden;
  }

  /* front */
  .front-title { position: absolute; top: 48px; left: 0; right: 0; text-align: center; }
  .title-main {
    font-family: "Bebas Neue", sans-serif; font-weight: 400; color: var(--gold);
    font-size: 112px; line-height: 0.9; letter-spacing: 2px;
  }
  .title-mid {
    display: flex; align-items: center; justify-content: center; gap: 12px;
    font-size: 20px; letter-spacing: 6px; text-transform: uppercase; margin: 8px 0 4px;
  }
  .title-mid::before, .title-mid::after { content: ""; width: 34px; height: 2px; background: var(--ink); }
  .title-lower {
    font-family: "Bebas Neue", sans-serif; color: var(--gold);
    font-size: 54px; line-height: 1; letter-spacing: 1px;
  }
  .subtitle { font-size: 12px; letter-spacing: 1.5px; text-transform: uppercase; margin-top: 10px; }
  .front-visual {
    position: absolute; left: 75px; top: 300px; width: 270px; height: 245px;
    background: radial-gradient(ellipse at 50% 40%, #f2f2f3 0%, var(--stone) 45%, var(--coin) 85%, rgba(183,178,147,0) 100%);
    border-radius: 45% 45% 40% 40%;
  }
  .author { position: absolute; left: 0; right: 0; text-align: center; font-size: 17px; letter-spacing: 4px; text-transform: uppercase; }
  .front .author { bottom: 26px; }

  /* back */
  .back-panel {
    position: absolute; left: 52px; right: 0; top: 70px;
    background: var(--panel); padding: 24px 30px 22px 34px;
  }
  .back-title {
    font-size: 18px; font-weight: 700; letter-spacing: 1px; text-transform: uppercase;
    text-align: center; line-height: 1.25;
  }
  .blurb { margin-top: 22px; font-size: 13.5px; line-height: 1.55; text-align: justify; }
  .back-panel .author { position: static; text-align: left; margin-top: 28px; font-size: 14px; letter-spacing: 2.5px; }
  .back-visual {
    position: absolute; left: 60px; bottom: 8px; width: 230px; height: 130px;
    background: radial-gradient(ellipse at 50% 45%, var(--coin) 0%, #cfcbb2 55%, rgba(207,203,178,0) 100%);
  }
</style>
</head>
<body>
  <section class="cover back" aria-label="Rückseite">
    <div class="back-panel">
      <h2 class="back-title">Der Pfad der klaren<br>Vermögensführung</h2>
      <p class="blurb">Haben Sie sich schon immer gefragt, was es für eine klare Vermögensführung braucht und wie es Ihnen gelingen kann, in den Zustand von Fülle zu kommen? Wussten Sie, dass es eine Verbindung zwischen innerer Ruhe und Wohlstand gibt? Möchten Sie wissen, wie Sie in den Geldfluss kommen können und auf welche Art und Weise sich Ihr finanzielles Handeln langfristig zum Positiven verändert? Dann lesen Sie jetzt dieses Buch!</p>
      <p class="author">Autor Name</p>
    </div>
    <div class="back-visual" role="img" aria-label="Foto: Schmetterling auf einem Häufchen Münzen"></div>
  </section>

  <section class="cover front" aria-label="Vorderseite">
    <header class="front-title">
      <h1 class="title-main">Der Pfad</h1>
      <p class="title-mid">der klaren</p>
      <p class="title-lower">Vermögensführung</p>
      <p class="subtitle">- Innere Ruhe und Wohlstand vereint -</p>
    </header>
    <div class="front-visual" role="img" aria-label="Foto: Schmetterling auf gestapelten weißen Steinen zwischen Münzen im geharkten Sand"></div>
    <p class="author">Autor Name</p>
  </section>
</body>
</html>
```